vireLattice "organisation chart"

We need a new Organisation Chart for our Company! We are actually in a Change-management-process and will Change from a hierarchical Organisation in to a Network Organisation. Therefor we need a new Organisation Chart.
The following departements must be visible and legible on the Chart:
Team Sales & Consulting
Team Productmanagement
Team Supply Chain
Team Human Resources
Team Smart Digital Development
Team Marketing & Communication
The title of the Chart ist «vireLattice»
The Colors of the back of the Chart must be: RGB 73/25/102 // Pantone 2627
The Colors for the different Teams should be:
Team Sales & Consulting (Pantone: 803/neon yellow = Background)
Team Productmanagement (Pantone: 804/neon orange = Background)
Team Supply Chain (Pantone: 802/neon green = Background)
Team Human Resources (Pantone: 801/neon blue = Background)
Team Smart Digital Development (Pantone: 805/neon red = Background)
Team Marketing & Communication (Pantone: 803/neon pink = Background)
See below (upload files) an example showing a self-made Chart ... :-)
Our font is: Univers LT Std // Please feel free to Combine the Fonts Colors with the background colors
It Company

```html
<!DOCTYPE html>
<html lang="en">
<head>
<meta charset="utf-8">
<title>vireLattice – Organisation Chart</title>
<link rel="stylesheet" href="https://fonts.googleapis.com/css2?family=Roboto+Condensed:wght@400;700&display=swap">
<style>
  :root {
    --page-bg: #ececec;
    --brand-purple: #491966;
    --brand-glow: #9a2b9e;
    --ring-dark: #4a2466;
    --ring-light: #a592bd;
    --arrow: #3d1f5c;
    --foot-grey: #d2d3d5;
    --panel: #ffffff;
    --team-sales: #e1e650;
    --team-product: #f58220;
    --team-supply: #77c043;
    --team-hr: #4f7fc4;
    --team-digital: #e8294f;
    --team-marketing: #d63a95;
    --ink-dark: #1a1a1a;
    --ink-light: #ffffff;
  }
  * { margin: 0; padding: 0; box-sizing: border-box; }
  html, body {
    width: 1200px; height: 1137px; overflow: hidden;
    background: var(--page-bg);
    font-family: "Roboto Condensed", "Arial Narrow", sans-serif;
  }
  .chart-card {
    position: absolute; left: 40px; top: 137px;
    width: 1120px; height: 862px;
    background: var(--foot-grey);
  }
  .chart-card__band {
    position: absolute; left: 0; top: 0; width: 100%; height: 709px;
    background: linear-gradient(to bottom,
      var(--brand-purple) 0%, var(--brand-purple) 62%,
      var(--brand-glow) 71%, var(--brand-purple) 80%, var(--brand-purple) 100%);
  }
  .chart-card__title {
    position: absolute; right: 76px; top: 32px;
    display: flex; align-items: center; gap: 12px;
    color: var(--ink-light); font-size: 32px; font-weight: 400;
    letter-spacing: 1px; line-height: 1;
  }
  .chart-card__title-dot {
    width: 14px; height: 14px; border-radius: 50%;
    background: var(--ink-light);
  }
  .chart-card__panel {
    position: absolute; left: 74px; top: 100px;
    width: 970px; height: 690px;
    background: var(--panel); border-radius: 8px;
    box-shadow: 0 2px 6px rgba(0,0,0,0.25);
  }
  .chart-card__panel svg { display: block; width: 100%; height: 100%; }
  .team-label {
    font-family: "Roboto Condensed", "Arial Narrow", sans-serif;
    font-weight: 700; font-size: 12px; text-anchor: middle;
  }
  .team-label--dark { fill: var(--ink-dark); }
  .team-label--light { fill: var(--ink-light); }
  .link { fill: none; stroke: var(--arrow); stroke-width: 1.3; stroke-dasharray: 4 3; }
</style>
</head>
<body>
<main class="chart-card">
  <div class="chart-card__band"></div>
  <h1 class="chart-card__title"><span class="chart-card__title-dot" aria-hidden="true"></span>vireLattice</h1>
  <section class="chart-card__panel" aria-label="Network organisation chart">
    <svg viewBox="0 0 613 436" xmlns="http://www.w3.org/2000/svg">
      <defs>
        <marker id="arrowhead" viewBox="0 0 10 10" refX="8" refY="5" markerWidth="6" markerHeight="6" orient="auto-start-reverse">
          <path d="M0 0 L10 5 L0 10 z" fill="var(--arrow)"/>
        </marker>
        <filter id="node-shadow" x="-20%" y="-20%" width="140%" height="140%">
          <feDropShadow dx="0" dy="1.5" stdDeviation="2" flood-color="#000" flood-opacity="0.35"/>
        </filter>
      </defs>

      <circle class="ring" cx="306" cy="221" r="157" fill="none" stroke="var(--ring-dark)" stroke-width="14"/>
      <path d="M257 72 A157 157 0 0 1 355 72" fill="none" stroke="var(--ring-light)" stroke-width="14"/>
      <path d="M257 370 A157 157 0 0 0 355 370" fill="none" stroke="var(--ring-light)" stroke-width="14"/>

      <line class="link" x1="222" y1="222" x2="392" y2="222" marker-start="url(#arrowhead)" marker-end="url(#arrowhead)"/>
      <line class="link" x1="262" y1="147" x2="350" y2="298" marker-start="url(#arrowhead)" marker-end="url(#arrowhead)"/>
      <line class="link" x1="357" y1="147" x2="262" y2="298" marker-start="url(#arrowhead)" marker-end="url(#arrowhead)"/>

      <path class="link" d="M278 38 Q306 28 334 38" marker-start="url(#arrowhead)" marker-end="url(#arrowhead)"/>
      <path class="link" d="M452 104 Q474 124 482 158" marker-start="url(#arrowhead)" marker-end="url(#arrowhead)"/>
      <path class="link" d="M482 286 Q474 320 452 340" marker-start="url(#arrowhead)" marker-end="url(#arrowhead)"/>
      <path class="link" d="M334 406 Q306 416 278 406" marker-start="url(#arrowhead)" marker-end="url(#arrowhead)"/>
      <path class="link" d="M160 340 Q138 320 130 286" marker-start="url(#arrowhead)" marker-end="url(#arrowhead)"/>
      <path class="link" d="M130 158 Q138 124 160 104" marker-start="url(#arrowhead)" marker-end="url(#arrowhead)"/>

      <g class="team team--sales">
        <circle cx="225" cy="85" r="54" fill="var(--team-sales)" stroke="#fff" stroke-width="4" filter="url(#node-shadow)"/>
        <text class="team-label team-label--dark" x="225" y="83">Team Sales</text>
        <text class="team-label team-label--dark" x="225" y="97">&amp; Consulting</text>
      </g>
      <g class="team team--product">
        <circle cx="379" cy="85" r="54" fill="var(--team-product)" stroke="#fff" stroke-width="4" filter="url(#node-shadow)"/>
        <text class="team-label team-label--dark" x="379" y="83">Team Product</text>
        <text class="team-label team-label--dark" x="379" y="97">Management</text>
      </g>
      <g class="team team--supply">
        <circle cx="464" cy="222" r="54" fill="var(--team-supply)" stroke="#fff" stroke-width="4" filter="url(#node-shadow)"/>
        <text class="team-label team-label--dark" x="464" y="219">Team</text>
        <text class="team-label team-label--dark" x="464" y="233">Supply Chain</text>
      </g>
      <g class="team team--hr">
        <circle cx="384" cy="357" r="54" fill="var(--team-hr)" stroke="#fff" stroke-width="4" filter="url(#node-shadow)"/>
        <text class="team-label team-label--light" x="384" y="354">Team Human</text>
        <text class="team-label team-label--light" x="384" y="368">Resources</text>
      </g>
      <g class="team team--digital">
        <circle cx="226" cy="357" r="54" fill="var(--team-digital)" stroke="#fff" stroke-width="4" filter="url(#node-shadow)"/>
        <text class="team-label team-label--light" x="226" y="347">Team Smart</text>
        <text class="team-label team-label--light" x="226" y="361">Digital</text>
        <text class="team-label team-label--light" x="226" y="375">Development</text>
      </g>
      <g class="team team--marketing">
        <circle cx="149" cy="222" r="54" fill="var(--team-marketing)" stroke="#fff" stroke-width="4" filter="url(#node-shadow)"/>
        <text class="team-label team-label--light" x="149" y="219">Team Marketing</text>
        <text class="team-label team-label--light" x="149" y="233">&amp; Communication</text>
      </g>
    </svg>
  </section>
</main>
</body>
</html>
```